Brochure for a shopping mall

looking for brochure design to market a shopping center for tenants to lease space from us landlords.

THE IDEA IS TO PROMOTE THIS shopping MALL AS a LUXURY ELEGANT SPACE FOR TENANTS. Spaces are available for retail stores as well as Offices and medical and dental offices

PLAN IS TO PRINT ON PRESSLEAF.COM 25.5" x 11" TEMPLATE. I uploaded a basic plan. But i want you to do

GREY HARROW MALL
2738 GREY HARROW BLVD
ALPHARETTA GA 30005

FOR LEASE 404 617 2284

PLEASE DOWNLOAD PHOTOS FROM THIS LINK
http://www.quorela.com/2014/04/Building-Photos-3/n-8K4rw/
Updates

Guys,

This is a committed project. 
Kindly send in your designs. We are looking for a luxury look to showcase this mall as a high end place

The small design I posted can be changed anyway. Use your imagination to make all the changes. 
The design should be able to be printed on 25.5" X 11 format on pressleaf.com.

I also need to include SOME MINOR details  like a small mapzio map and number of parking spaces 262 traffic count.

some description of building like
Italian Florence Dome design with French architecture influence, newly built in 2007.
Imported Limestone walls and flooring and Mediterranean tiles.
Ideally suited for Retail store or office space including medical and dental offices.
A Class "A" building in Class "A" location

I am looking for front and back designs for the 25.5 inches X 11 inches TRIFOLD brochures.

Reason: No more extensions after this deadline. I really need something with a Luxury Look. on a trifold pattern. Only One goal of the Brochure is to attract New Tenants to rent space fro this shopping center

Reason: No more designs are being accepted. We will invite 2 designers to provide final designs and finalize one. Thank You for wonderful job

Reason: No new designs are being accepted. This is to finalize existing designs only

```html
<!DOCTYPE html>
<html lang="en">
<head>
<meta charset="utf-8">
<title>Grey Harrow Mall – Leasing Brochure</title>
<link href="https://fonts.googleapis.com/css2?family=Nunito+Sans:wght@200;300;400;700;800&display=swap" rel="stylesheet">
<style>
  :root {
    --teal: #4aa8b0;
    --sage: #d6e3c5;
    --tan: #efb479;
    --salmon: #f59a7a;
    --band-grey: rgba(150, 178, 176, 0.82);
    --band-orange: rgba(232, 118, 50, 0.9);
    --box-dark: rgba(40, 40, 40, 0.72);
    --ink: #3b3b3b;
    --white: #ffffff;
  }
  * { margin: 0; padding: 0; box-sizing: border-box; }
  html, body { width: 1200px; height: 520px; overflow: hidden; background: #fff; }
  .brochure {
    position: relative; width: 1200px; height: 520px; overflow: hidden;
    font-family: "Nunito Sans", Arial, sans-serif; color: var(--white);
  }
  .panel { position: absolute; top: 0; height: 520px; width: 400px; overflow: hidden; }
  .panel--exterior { left: 0; }
  .panel--interior { left: 400px; }
  .panel--cover { left: 800px; background: var(--white); }

  .photo { position: absolute; inset: 0; }
  .photo--exterior {
    background: linear-gradient(180deg, #3f7fc9 0%, #7fb0e0 35%, #e9e7e0 55%, #d8d4cc 75%, #c9c3b6 100%);
  }
  .photo--interior {
    background: linear-gradient(180deg, #5a4a3a 0%, #efe8dc 30%, #d9d3c6 48%, #b8733a 65%, #8a4a20 100%);
  }

  .word-band {
    position: absolute; top: 0; height: 520px;
    writing-mode: vertical-rl; font-weight: 200; color: var(--white);
    display: flex; align-items: center; line-height: 1;
  }
  .word-band--luxurious { left: 256px; width: 144px; background: var(--band-grey); font-size: 96px; padding-top: 6px; }
  .word-band--imaginative { left: 257px; width: 143px; background: var(--band-orange); font-size: 88px; padding-top: 12px; }

  .info-box { position: absolute; background: var(--box-dark); padding: 10px 8px 8px; }
  .info-box--location { left: 12px; top: 300px; width: 226px; height: 138px; }
  .info-box--leasing { left: 10px; top: 18px; width: 226px; height: 154px; }
  .info-box h2 { font-weight: 800; font-size: 18px; line-height: 1.1; letter-spacing: 0.2px; }
  .info-box p { font-weight: 700; font-size: 10.5px; line-height: 1.3; margin-top: 6px; }
  .info-box .phone { font-weight: 800; font-size: 18px; margin-top: 10px; }

  .stripe { position: absolute; left: 0; width: 400px; }
  .stripe--sage { top: 103px; height: 16px; background: var(--sage); }
  .stripe--teal { top: 119px; height: 6px; background: var(--teal); }
  .photo--night {
    position: absolute; left: 0; top: 125px; width: 400px; height: 145px;
    background: linear-gradient(180deg, #1c2a5a 0%, #2c3f78 50%, #b39a72 70%, #3a3a3e 100%);
  }
  .tagline {
    position: absolute; left: 9px; top: 277px; font-size: 20.5px; font-weight: 400;
    color: var(--teal); white-space: nowrap;
  }
  .tagline .dot { display: inline-block; width: 6px; height: 6px; background: var(--teal); vertical-align: middle; margin: 0 3px; }
  .colour-bar { position: absolute; left: 0; top: 306px; width: 400px; height: 22px; display: flex; }
  .colour-bar span { height: 100%; }
  .c-teal { width: 100px; background: var(--teal); }
  .c-sage { width: 102px; background: var(--sage); }
  .c-tan { width: 102px; background: var(--tan); }
  .c-salmon { width: 96px; background: var(--salmon); }

  .brand { position: absolute; right: 18px; top: 400px; text-align: right; color: var(--ink); font-weight: 300; }
  .brand-name { font-size: 30px; line-height: 1.05; letter-spacing: 1px; }
  .address {
    position: absolute; left: 198px; top: 470px; color: var(--ink);
    font-weight: 700; font-size: 11px; line-height: 1.35; font-style: normal;
  }
</style>
</head>
<body>
<main class="brochure">
  <section class="panel panel--exterior">
    <div class="photo photo--exterior" role="img" aria-label="Photo of the mall's white stone tower and storefront under a blue sky"></div>
    <div class="word-band word-band--luxurious">luxurious</div>
    <div class="info-box info-box--location">
      <h2>AN IDEAL LOCATION FOR YOUR BUSINESS</h2>
      <p>Shoppers in the area have an average household income of $137,000. Grey Harrow Mall is located in a great area with an average traffic count of 54,000 a day.</p>
    </div>
  </section>

  <section class="panel panel--interior">
    <div class="photo photo--interior" role="img" aria-label="Photo of an empty lease space with glass storefront and polished stone floor"></div>
    <div class="info-box info-box--leasing">
      <h2>SPACES AVAILABLE FOR RETAIL, OFFICE MEDICAL &amp; DENTAL</h2>
      <p>Now leasing spaces from<br>1,176 to 15,000 sq. ft.</p>
      <p class="phone">CALL (404) 617.2284</p>
    </div>
    <div class="word-band word-band--imaginative">imaginative</div>
  </section>

  <section class="panel panel--cover">
    <div class="stripe stripe--sage"></div>
    <div class="stripe stripe--teal"></div>
    <div class="photo--night" role="img" aria-label="Night photo of the illuminated shopping center and parking lot"></div>
    <p class="tagline">elegant<span class="dot"></span>luxurious<span class="dot"></span>vibrant<span class="dot"></span>imaginative</p>
    <div class="colour-bar"><span class="c-teal"></span><span class="c-sage"></span><span class="c-tan"></span><span class="c-salmon"></span></div>
    <div class="brand">
      <div class="brand-name">GREY HARROW<br>MALL</div>
    </div>
    <address class="address">2738 Grey Harrow Blvd.<br>Larkmoor, GA 30172</address>
  </section>
</main>
</body>
</html>
```